Sunvale Energy UK Flyer Design, for local domestic and commercial properties.

We are a renewable energy company called "SUNVALE ENERGY UK" we specialize in
Electrical and renewable energy project consultancy.
Solar panel installations
battery storage.
Electrical design and installation from Stage 3

Details can be found on our website: www.sunvaleenergyuk.co.uk
Am looking to have a flyer designed so we can have printed and delivered to all local areas.
We carry out free project surveys and offer full project transparency through out the clients journey.
attached is our logo of which i hope may help.

Target Market(s)

Domestic and commercial properties looking to dramatically reduce energy bills

Industry/Entity Type

Domestic, commercial, industrial, mixed used development and much more.

Font styles to use
Serif
Sans Serif
Decorative

Colors
FFC000
F8CF3A
FAE287
FDF2CF
FEFAEE
F0912C
F2A743
F7CA91
FBE8D2
FDF5EE
EE7325
F08F49
F5BC92
FAE3D3
FDF4ED

Requirements
Must have
• Highlight we offer free quotations and offer a fully transparent project processes from design, installation Plus leading health and safety process no matter what size project.
Nice to have
• Pictures of solar panel systems, i have attached a few pictures which you may wish to edit or take snippets etc.

```html
<!DOCTYPE html>
<html lang="en">
<head>
<meta charset="utf-8">
<title>Sunvale Energy UK Flyer</title>
<link href="https://fonts.googleapis.com/css2?family=Marcellus&family=Crimson+Text:wght@400;600&display=swap" rel="stylesheet">
<style>
  :root{
    --stage:#4a4a4a;
    --black:#000000;
    --orange:#f5901c;
    --orange-deep:#e07a10;
    --cream:#fdf2cf;
    --white:#ffffff;
    --ink:#1a1a1a;
    --sky:#9cc3e6;
    --panel:#1d2740;
  }
  *{margin:0;padding:0;box-sizing:border-box;}
  html,body{width:976px;height:1200px;overflow:hidden;background:var(--stage);}
  .flyer{
    position:absolute;left:63.5px;top:0;width:827px;height:1169px;
    transform:scale(1.02652);transform-origin:0 0;
    background:var(--black);overflow:hidden;
    font-family:'Crimson Text',serif;
  }
  .hero-photo{
    position:absolute;left:0;top:0;width:827px;height:560px;
    background:
      linear-gradient(200deg,#ffffff 0%,rgba(255,255,255,.9) 22%,rgba(255,255,255,0) 45%),
      linear-gradient(180deg,var(--sky) 0%,#c9dbe9 38%,#3a4a6a 55%,var(--panel) 100%);
  }
  .brand{
    position:absolute;right:52px;top:120px;text-align:center;
    font-family:'Marcellus',serif;color:var(--ink);
  }
  .brand-mark{width:46px;height:46px;border-radius:50%;background:var(--orange);margin:0 auto 16px;}
  .brand-name{font-size:30px;letter-spacing:3px;line-height:1.1;}
  .curve{position:absolute;left:0;top:300px;}
  .badge{
    position:absolute;border-radius:50%;border:12px solid var(--orange);overflow:hidden;
  }
  .badge .photo{width:100%;height:100%;}
  .badge-left{left:44px;top:327px;width:216px;height:216px;}
  .badge-left .photo{background:linear-gradient(135deg,#d9cbb8,#efe9e2 45%,#8a6d52);}
  .badge-mid{left:270px;top:316px;width:290px;height:290px;}
  .badge-mid .photo{background:linear-gradient(170deg,#6f9fd6 0%,#a9c6e6 30%,#1e2536 55%,#2b3246 75%,#b85c3a 100%);}
  .badge-right{left:570px;top:327px;width:216px;height:216px;}
  .badge-right .photo{background:linear-gradient(150deg,#cfd9e4 0%,#7a8aa6 35%,#1f2a44 70%,#334160 100%);}
  .headline{
    position:absolute;left:0;width:827px;text-align:center;font-family:'Marcellus',serif;
  }
  .headline-name{top:620px;font-size:46px;color:var(--orange);}
  .headline-rule{position:absolute;left:213px;top:677px;width:425px;height:2px;
    background:linear-gradient(90deg,#555,#c9c9b8,#555);}
  .headline-tag{top:684px;font-size:46px;color:var(--cream);}
  .col-title{position:absolute;top:752px;font-size:38px;color:var(--orange);font-weight:600;}
  .col-title.left{left:108px;}
  .col-title.right{left:515px;}
  .list{position:absolute;list-style:none;color:var(--white);}
  .list li{position:relative;line-height:30px;}
  .specialties{left:84px;top:815px;width:340px;font-size:23px;}
  .specialties li{padding-left:50px;margin-bottom:29px;}
  .specialties li::before{
    content:"";position:absolute;left:4px;top:8px;width:26px;height:26px;border-radius:50%;
    border:2px solid var(--white);
  }
  .offers{left:444px;top:817px;width:360px;font-size:26px;}
  .offers li{padding-left:52px;margin-bottom:18px;}
  .offers svg{position:absolute;left:0;top:4px;}
  .footer{
    position:absolute;left:0;top:1092px;width:827px;height:77px;background:var(--orange-deep);
    display:flex;align-items:center;color:var(--white);font-size:25px;
  }
  .contact-btn{
    margin-left:51px;width:180px;height:38px;border-radius:19px;background:var(--white);
    color:var(--ink);font-size:25px;display:flex;align-items:center;justify-content:center;
  }
  .footer-item{display:flex;align-items:center;gap:12px;}
  .phone{margin-left:21px;}
  .web{margin-left:18px;}
  .footer-icon{width:34px;height:34px;border-radius:50%;background:var(--white);display:flex;align-items:center;justify-content:center;}
</style>
</head>
<body>
<main class="flyer">
  <div class="hero-photo" role="img" aria-label="Two installers in hard hats and hi-vis vests lifting a solar panel on a rooftop array"></div>

  <div class="brand">
    <div class="brand-mark"></div>
    <div class="brand-name">SUNVALE<br>ENERGY UK</div>
  </div>

  <svg class="curve" width="827" height="260" viewBox="0 300 827 260" aria-hidden="true">
    <path d="M0 545 Q413 330 827 545 L827 560 L0 560 Z" fill="#000"/>
    <path d="M0 545 Q413 330 827 545 L827 560 L0 560 Z" fill="#000"/>
    <path d="M0 545 Q413 330 827 545" fill="none" stroke="#f5901c" stroke-width="10"/>
    <rect x="0" y="548" width="827" height="12" fill="#000"/>
  </svg>

  <div class="badge badge-left"><div class="photo" role="img" aria-label="Inverter and battery storage units mounted on a utility room wall"></div></div>
  <div class="badge badge-right"><div class="photo" role="img" aria-label="Close view of solar panels on a tiled roof"></div></div>
  <div class="badge badge-mid"><div class="photo" role="img" aria-label="House roof with black solar panels, chimney and scaffolding"></div></div>

  <h1 class="headline headline-name">SUNVALE ENERGY UK</h1>
  <div class="headline-rule"></div>
  <h2 class="headline headline-tag">RENEWABLE ENERGY</h2>

  <h3 class="col-title left">We specialize in</h3>
  <h3 class="col-title right">we offer</h3>

  <ul class="list specialties">
    <li>Electrical and renewable energy project consultancy.</li>
    <li>Solar panel installations battery storage.</li>
    <li>Electrical design and installation from Stage 3</li>
  </ul>

  <ul class="list offers">
    <li><svg width="34" height="34" viewBox="0 0 34 34"><circle cx="17" cy="17" r="15" fill="none" stroke="#fff" stroke-width="2.5"/><circle cx="17" cy="14" r="3" fill="#fff"/><circle cx="10.5" cy="16" r="2.4" fill="#fff"/><circle cx="23.5" cy="16" r="2.4" fill="#fff"/><rect x="7" y="20" width="20" height="4" rx="2" fill="#fff"/></svg>Free project surveys</li>
    <li><svg width="34" height="34" viewBox="0 0 34 34"><circle cx="17" cy="17" r="15" fill="none" stroke="#fff" stroke-width="2.5"/><rect x="11" y="9" width="12" height="15" rx="1" fill="none" stroke="#fff" stroke-width="2"/><path d="M14 19 l3 3 l5 -6" fill="none" stroke="#fff" stroke-width="2"/></svg>Free quotations</li>
    <li><svg width="34" height="34" viewBox="0 0 34 34"><circle cx="17" cy="17" r="15" fill="none" stroke="#fff" stroke-width="2.5"/><circle cx="17" cy="16" r="5" fill="none" stroke="#fff" stroke-width="2"/><path d="M9 24 q8 5 16 0" fill="none" stroke="#fff" stroke-width="2"/></svg>Fully transparent project, installation and health and safety process no matter what size project.</li>
  </ul>

  <footer class="footer">
    <div class="contact-btn">Contact Us</div>
    <div class="footer-item phone">
      <span class="footer-icon"><svg width="18" height="18" viewBox="0 0 24 24"><path d="M6.6 10.8a15 15 0 0 0 6.6 6.6l2.2-2.2a1 1 0 0 1 1-.25 11.4 11.4 0 0 0 3.6.57 1 1 0 0 1 1 1V20a1 1 0 0 1-1 1A17 17 0 0 1 3 4a1 1 0 0 1 1-1h3.5a1 1 0 0 1 1 1c0 1.25.2 2.45.57 3.57a1 1 0 0 1-.25 1z" fill="#111"/></svg></span>
      <span>0161-555-0142</span>
    </div>
    <div class="footer-item web">
      <span class="footer-icon"><svg width="20" height="20" viewBox="0 0 24 24" fill="none" stroke="#111" stroke-width="1.8"><circle cx="12" cy="12" r="9"/><ellipse cx="12" cy="12" rx="4" ry="9"/><path d="M3 12h18M4.5 7.5h15M4.5 16.5h15"/></svg></span>
      <span>www.sunvaleenergyuk.co.uk</span>
    </div>
  </footer>
</main>
</body>
</html>
```